Velvetorchid Hair & Beauty Business Card

Velvetorchid Hair & Beauty is a boutique salon located in the picturesque Lake Taupo NZ. The salon is very luxurious, opulent gold gilded mirrors, chandelier lit, contemporary french decor, sets the mood to create beautiful hair, makeup and all beauty services. Just had a new logo design and now after a new business card.
Logo
14 Kerewhenua Street
Taupo
Phone (07) 384 6139
www.velvetorchid.co.nz
email hair@velvetorchid.co.nz
Lorinda Feltham
Also need a space to put in Stylist name, date, appointment time. thanks;)
Another idea is we could incorporate the wallpaper in the back ground either on the back or front or use an ornate glided frame (around the edge of the card) like on my website where my brides photos flash.
Decided against the wall paper but at least you can see our colour theme for the salon.
Updates

Please check out my updated brief . Thanks :)

Target Market(s)

25-60 years plus, mainly mid age females , wanting the best possible service , high standard of workmanship and money not a problem.

Industry/Entity Type

Boutique

Requirements
Must have
• Gold and silver

```html
<!DOCTYPE html>
<html lang="en">
<head>
<meta charset="utf-8">
<title>Velvetorchid Hair &amp; Beauty – Business Card</title>
<link rel="stylesheet" href="https://fonts.googleapis.com/css2?family=EB+Garamond:ital,wght@0,400;1,400&display=swap">
<style>
  :root {
    --backdrop: #c6c6c6;
    --chocolate: #3b2214;
    --paper: #ffffff;
    --gold: #8a6d12;
    --gold-light: #d9a94a;
    --gold-deep: #b9812a;
    --contact: #5f4f42;
    --ink: #565656;
    --rule: #8c8c8c;
  }
  * { box-sizing: border-box; margin: 0; padding: 0; }
  html, body {
    width: 1200px; height: 900px; overflow: hidden;
    background: var(--backdrop);
    font-family: "EB Garamond", Georgia, serif;
  }
  .canvas { position: relative; width: 1200px; height: 900px; }
  .card { position: absolute; left: 255px; width: 690px; height: 347px; }
  .card--front { top: 79px; background: var(--chocolate); }
  .card--back { top: 474px; background: var(--paper); }

  .corner-ornament {
    position: absolute; width: 78px; height: 80px;
    background: radial-gradient(circle at 35% 35%, var(--gold-light), var(--gold-deep) 70%);
    opacity: .85;
  }
  .corner-ornament--tl { left: 25px; top: 23px; border-radius: 0 0 60% 0; }
  .corner-ornament--tr { right: 25px; top: 23px; border-radius: 0 0 0 60%; }
  .corner-ornament--bl { left: 25px; bottom: 23px; border-radius: 0 60% 0 0; }
  .corner-ornament--br { right: 25px; bottom: 23px; border-radius: 60% 0 0 0; }

  .crest-ornament {
    position: absolute; left: 213px; top: 43px; width: 267px; height: 62px;
    background: linear-gradient(180deg, #8a7112, #6c560e);
    border-radius: 50% 50% 40% 40% / 70% 70% 30% 30%;
    opacity: .9;
  }
  .brand {
    position: absolute; left: 0; width: 100%; text-align: center;
    color: var(--gold); font-weight: 400;
  }
  .brand__name { top: 106px; font-size: 64px; line-height: 1; letter-spacing: 1px; }
  .brand__tagline {
    top: 177px; font-size: 15px; letter-spacing: 1.5px; text-transform: uppercase;
    display: flex; align-items: center; justify-content: center; gap: 10px;
  }
  .brand__tagline::before, .brand__tagline::after {
    content: ""; width: 102px; height: 2px; background: var(--gold);
  }
  .contact {
    position: absolute; left: 0; width: 100%; top: 248px; text-align: center;
    font-style: italic; font-size: 20px; line-height: 27px; color: var(--contact);
  }

  .side-brand {
    position: absolute; left: 42px; top: 85px; width: 80px; height: 175px;
  }
  .side-brand__ornament {
    position: absolute; left: 4px; top: 20px; width: 34px; height: 140px;
    background: linear-gradient(90deg, #c9b04a, #8f7a1c);
    border-radius: 40%;
    opacity: .85;
  }
  .side-brand__text {
    position: absolute; left: 40px; top: 87px; width: 180px;
    transform: translate(-50%, -50%) rotate(-90deg) translateY(18px);
    text-align: center; color: var(--gold);
  }
  .side-brand__name { font-size: 30px; line-height: 1; }
  .side-brand__tagline {
    font-size: 8px; letter-spacing: 1px; text-transform: uppercase;
    border-top: 1px solid var(--gold); margin: 3px 12px 0; padding-top: 2px;
  }

  .appointment {
    position: absolute; left: 172px; top: 100px; width: 402px;
    list-style: none;
  }
  .appointment__row {
    display: flex; align-items: center; height: 58px;
    font-size: 27px; color: var(--ink);
  }
  .appointment__label { width: 91px; text-align: center; }
  .appointment__line {
    flex: 1; margin-left: 0; margin-top: 8px;
    border-bottom: 1.5px dashed var(--rule);
  }
</style>
</head>
<body>
<main class="canvas">
  <section class="card card--front" aria-label="Business card front">
    <div class="corner-ornament corner-ornament--tl" role="img" aria-label="Gold filigree corner ornament"></div>
    <div class="corner-ornament corner-ornament--tr" role="img" aria-label="Gold filigree corner ornament"></div>
    <div class="corner-ornament corner-ornament--bl" role="img" aria-label="Gold filigree corner ornament"></div>
    <div class="corner-ornament corner-ornament--br" role="img" aria-label="Gold filigree corner ornament"></div>
    <div class="crest-ornament" role="img" aria-label="Gold baroque scroll ornament above the salon name"></div>
    <h1 class="brand brand__name">Velvetorchid</h1>
    <p class="brand brand__tagline">Hair &amp; Beauty</p>
    <address class="contact">
      14 Kerewhenua Street /Taupo • Phone (07) 384 6139<br>
      www.velvetorchid.co.nz • email hair@velvetorchid.co.nz
    </address>
  </section>

  <section class="card card--back" aria-label="Business card back – appointment">
    <div class="corner-ornament corner-ornament--tl" role="img" aria-label="Gold filigree corner ornament"></div>
    <div class="corner-ornament corner-ornament--tr" role="img" aria-label="Gold filigree corner ornament"></div>
    <div class="corner-ornament corner-ornament--bl" role="img" aria-label="Gold filigree corner ornament"></div>
    <div class="corner-ornament corner-ornament--br" role="img" aria-label="Gold filigree corner ornament"></div>
    <div class="side-brand">
      <div class="side-brand__ornament" role="img" aria-label="Vertical gold baroque scroll ornament"></div>
      <div class="side-brand__text">
        <div class="side-brand__name">Velvetorchid</div>
        <div class="side-brand__tagline">Hair &amp; Beauty</div>
      </div>
    </div>
    <ul class="appointment">
      <li class="appointment__row"><span class="appointment__label">Stylist</span><span class="appointment__line"></span></li>
      <li class="appointment__row"><span class="appointment__label">Date</span><span class="appointment__line"></span></li>
      <li class="appointment__row"><span class="appointment__label">Time</span><span class="appointment__line"></span></li>
    </ul>
  </section>
</main>
</body>
</html>
```